Business Card Design for Tarlo Cosmetics

hair extension supplier and mobile technican
make up and make up artistry
cosmetic eye contacts
eye lashes
general facial and hair products

```html
<!DOCTYPE html>
<html lang="en">
<head>
<meta charset="utf-8">
<title>Tarlo Cosmetics – Business Card</title>
<link href="https://fonts.googleapis.com/css2?family=Jost:wght@300;400&family=Cookie&display=swap" rel="stylesheet">
<style>
  :root {
    --page: #ffffff;
    --card-black: #000000;
    --card-lift: #262626;
    --ink: #ffffff;
    --ink-soft: #d9d9d9;
    --ghost: rgba(255,255,255,0.07);
    --rule: rgba(255,255,255,0.35);
    --hair: #5a4034;
    --lashes: #b0703c;
    --nails: #d9584f;
    --eyes: #3f9a4a;
    --tile-edge: #cfcfcf;
  }
  * { margin: 0; padding: 0; box-sizing: border-box; }
  html, body { width: 1200px; height: 780px; overflow: hidden; background: var(--page); }
  body { position: relative; font-family: 'Jost', sans-serif; color: var(--ink); }

  .card { position: absolute; overflow: hidden; background: var(--card-black); }
  .card--front {
    left: 49px; top: 77px; width: 624px; height: 357px;
    background: linear-gradient(180deg, #000 0%, #000 55%, var(--card-lift) 80%, #111 100%);
  }
  .card--back {
    left: 704px; top: 20px; width: 402px; height: 704px;
    background: linear-gradient(160deg, #000 0%, #0b0b0b 35%, #262626 62%, #0c0c0c 85%, #000 100%);
  }

  .brand { position: absolute; left: 0; right: 0; text-align: center; font-weight: 300; color: var(--ink); }
  .brand__name { display: block; line-height: 1; }
  .brand__sub { display: block; line-height: 1; }

  .card--front .brand { top: 34px; }
  .card--front .brand__name { font-size: 84px; letter-spacing: 0.32em; padding-left: 0.32em; }
  .card--front .brand__sub { margin-top: 36px; font-size: 24px; letter-spacing: 0.75em; padding-left: 0.75em; }

  .card--back .brand { top: 22px; }
  .card--back .brand__name { font-size: 30px; letter-spacing: 0.3em; padding-left: 0.3em; }
  .card--back .brand__sub { margin-top: 5px; font-size: 9px; letter-spacing: 0.75em; padding-left: 0.75em; }

  .services { position: absolute; display: flex; justify-content: space-between; }
  .card--front .services { left: 103px; width: 418px; top: 246px; }
  .card--back .services { left: 42px; width: 324px; top: 98px; }

  .service { display: flex; flex-direction: column; align-items: center; }
  .service__thumb { border-radius: 9px; border: 2px solid var(--tile-edge); }
  .card--front .service__thumb { width: 76px; height: 56px; }
  .card--back .service__thumb { width: 58px; height: 44px; border-radius: 7px; }
  .service__label { color: var(--ink-soft); font-weight: 400; white-space: nowrap; }
  .card--front .service__label { font-size: 13px; margin-top: 6px; }
  .card--back .service__label { font-size: 9px; margin-top: 4px; }

  .thumb--hair { background: linear-gradient(135deg, #e9d6c8 0%, var(--hair) 55%, #2a1c16 100%); }
  .thumb--lashes { background: radial-gradient(circle at 45% 50%, #3a2412 0%, var(--lashes) 40%, #e8c9a4 100%); }
  .thumb--nails { background: linear-gradient(135deg, #f3c2b5 0%, var(--nails) 55%, #b2332e 100%); }
  .thumb--eyes { background: radial-gradient(circle at 50% 50%, #111 0%, var(--eyes) 28%, #7cc77a 55%, #f4f4f4 80%); }

  .rule { position: absolute; height: 1px; background: linear-gradient(90deg, transparent, var(--rule) 20%, var(--rule) 80%, transparent); }
  .card--front .rule { left: 80px; right: 80px; top: 232px; opacity: 0.4; }

  .ghost-brand {
    position: absolute; left: -40px; top: 210px; width: 520px;
    font-weight: 300; color: var(--ghost); line-height: 1;
  }
  .ghost-brand__name { display: block; font-size: 150px; letter-spacing: 0.18em; }
  .ghost-brand__sub { display: block; margin-top: 12px; font-size: 46px; letter-spacing: 0.6em; }

  .contact { position: absolute; left: 0; right: 0; }
  .contact .rule { position: relative; margin: 0 16px 0 34px; }
  .contact--person { top: 504px; }
  .contact__name { font-family: 'Cookie', cursive; font-size: 38px; text-align: right; padding-right: 24px; margin-top: 6px; line-height: 1; }
  .contact__address { font-size: 17px; text-align: right; padding-right: 24px; margin-top: 4px; }

  .contact--reach { top: 588px; }
  .contact__social { position: absolute; left: 32px; top: 22px; width: 42px; height: 42px; border-radius: 5px; background: linear-gradient(180deg, #6c6c6c, #3e3e3e); }
  .contact__line { display: flex; justify-content: flex-end; align-items: center; gap: 10px; padding-right: 22px; font-size: 17px; }
  .contact__line:first-of-type { margin-top: 14px; }
  .contact__line + .contact__line { margin-top: 6px; }
  .icon { fill: none; stroke: var(--ink); stroke-width: 1.4; }
</style>
</head>
<body>

<section class="card card--front" aria-label="Business card front">
  <div class="brand">
    <span class="brand__name">TARLO</span>
    <span class="brand__sub">COSMETICS</span>
  </div>
  <div class="rule"></div>
  <ul class="services" style="list-style:none">
    <li class="service"><div class="service__thumb thumb--hair" role="img" aria-label="Photo of long dark glossy hair"></div><span class="service__label">Tarlo Hair</span></li>
    <li class="service"><div class="service__thumb thumb--lashes" role="img" aria-label="Close-up photo of long eyelashes"></div><span class="service__label">Tarlo Lashes</span></li>
    <li class="service"><div class="service__thumb thumb--nails" role="img" aria-label="Photo of red painted nails"></div><span class="service__label">Tarlo Nails</span></li>
    <li class="service"><div class="service__thumb thumb--eyes" role="img" aria-label="Close-up photo of a green eye"></div><span class="service__label">Tarlo Eyes</span></li>
  </ul>
</section>

<section class="card card--back" aria-label="Business card back">
  <div class="ghost-brand" aria-hidden="true">
    <span class="ghost-brand__name">TARLO</span>
    <span class="ghost-brand__sub">COSMETICS</span>
  </div>
  <div class="brand">
    <span class="brand__name">TARLO</span>
    <span class="brand__sub">COSMETICS</span>
  </div>
  <ul class="services" style="list-style:none">
    <li class="service"><div class="service__thumb thumb--hair" role="img" aria-label="Photo of long dark glossy hair"></div><span class="service__label">Tarlo Hair</span></li>
    <li class="service"><div class="service__thumb thumb--lashes" role="img" aria-label="Close-up photo of long eyelashes"></div><span class="service__label">Tarlo Lashes</span></li>
    <li class="service"><div class="service__thumb thumb--nails" role="img" aria-label="Photo of red painted nails"></div><span class="service__label">Tarlo Nails</span></li>
    <li class="service"><div class="service__thumb thumb--eyes" role="img" aria-label="Close-up photo of a green eye"></div><span class="service__label">Tarlo Eyes</span></li>
  </ul>

  <div class="contact contact--person">
    <div class="rule"></div>
    <p class="contact__name">Mara Benton</p>
    <p class="contact__address">18 Marlow st, Eastfield, WA, 6010</p>
  </div>

  <div class="contact contact--reach">
    <div class="rule"></div>
    <div class="contact__social" aria-label="Social page"></div>
    <p class="contact__line">0400 55 12 37
      <svg class="icon" width="14" height="24" viewBox="0 0 14 24" aria-hidden="true"><rect x="1" y="1" width="12" height="22" rx="2"/><rect x="3" y="4" width="8" height="12"/><circle cx="7" cy="19.5" r="1.2"/></svg>
    </p>
    <p class="contact__line">mara@tarlocosmetics.com.au
      <svg class="icon" width="20" height="14" viewBox="0 0 20 14" aria-hidden="true"><rect x="1" y="1" width="18" height="12"/><path d="M1 1 L10 8 L19 1"/></svg>
    </p>
  </div>
</section>

</body>
</html>
```